Brookvane Eyecare Optometrists

News paper advertisement (150mm H x 110mm W).
Eye testing (Tallacor covered).
Prescription glasses,sunglasses & contact lenses.
All major health funds accepted.
Phone: 94517038 for an appointment at our Claremont practice
or Phone: 95643218 for an appointment at our Subiaco practice.
Please disregard "Good health for less" slogan.
We are an independent Optometry practice providing major fashion brands in both Optical frames & sunglasses.
Keep it simple and / or entertaining.
Use of company logo not critical, only discretionary.
Use as much or as little of this information as you wish.

```html
<!DOCTYPE html>
<html lang="en">
<head>
<meta charset="utf-8">
<title>Brookvane Eyecare – Newspaper Advertisement</title>
<link rel="stylesheet" href="https://fonts.googleapis.com/css2?family=Delius&family=Patrick+Hand&display=swap">
<style>
  :root {
    --page-bg: #ececec;
    --card-teal: #6db0b2;
    --bubble-white: #f4f4f2;
    --ink: #1e1e1e;
    --accent-red: #c8141e;
    --sun-yellow: #f2dc1c;
    --art-tone: #9c8a80;
  }
  * { margin: 0; padding: 0; box-sizing: border-box; }
  html, body {
    width: 1200px;
    height: 1000px;
    overflow: hidden;
    background: var(--page-bg);
  }
  .ad-card {
    position: absolute;
    left: 51px;
    top: 101px;
    width: 844px;
    height: 613px;
    transform: scale(1.3);
    transform-origin: 0 0;
    background: var(--card-teal);
    overflow: hidden;
  }
  .speech-bubble {
    position: absolute;
    left: 0;
    top: 0;
    width: 844px;
    height: 613px;
  }
  .intro-quote {
    position: absolute;
    left: 0;
    top: 36px;
    width: 590px;
    font-family: "Delius", sans-serif;
    font-size: 25px;
    line-height: 35px;
    color: var(--ink);
    text-align: center;
  }
  .idea-icon {
    position: absolute;
    left: 272px;
    top: 146px;
    width: 46px;
    height: 76px;
  }
  .service-list {
    position: absolute;
    left: 0;
    top: 232px;
    width: 610px;
    list-style: none;
    font-family: "Patrick Hand", cursive;
    font-size: 30px;
    line-height: 35px;
    color: var(--ink);
    text-transform: uppercase;
    text-align: center;
    letter-spacing: 0.5px;
  }
  .service-list li { margin-bottom: 12px; }
  .service-list .bullet { color: var(--accent-red); margin-right: 8px; }
  .brand-mark {
    position: absolute;
    left: 600px;
    top: 14px;
    width: 66px;
    height: 66px;
    border-radius: 50%;
    background: var(--sun-yellow);
  }
  .brand-name {
    position: absolute;
    left: 620px;
    top: 92px;
    width: 210px;
    font-family: "Patrick Hand", cursive;
    font-size: 34px;
    line-height: 34px;
    color: var(--ink);
    text-align: center;
    text-transform: uppercase;
    letter-spacing: 2px;
  }
  .illustration-slot {
    position: absolute;
    left: 606px;
    top: 284px;
    width: 238px;
    height: 329px;
    background: var(--art-tone);
  }
  .contact-box {
    position: absolute;
    left: 27px;
    top: 506px;
    width: 517px;
    height: 80px;
    background: var(--bubble-white);
    border: 2px solid var(--ink);
    font-family: "Patrick Hand", cursive;
    font-size: 21px;
    line-height: 30px;
    color: var(--ink);
    text-transform: uppercase;
  }
  .contact-box .phone-icon {
    position: absolute;
    left: 8px;
    top: 8px;
    width: 40px;
    height: 62px;
  }
  .contact-lines {
    position: absolute;
    left: 62px;
    top: 10px;
  }
  .contact-lines .number { color: var(--accent-red); font-weight: 700; letter-spacing: 1px; }
</style>
</head>
<body>
  <main class="ad-card">
    <svg class="speech-bubble" viewBox="0 0 844 613" aria-hidden="true">
      <path d="M 543.6 377 L 598 510 L 588.2 320.6 A 318 257 0 1 0 543.6 377 Z"
            fill="#f4f4f2" stroke="#1e1e1e" stroke-width="3" stroke-linejoin="round"/>
    </svg>

    <p class="intro-quote">„We are an independent Optometry<br>practice providing major fashion brands<br>in both Optical frames &amp; sunglasses.“</p>

    <svg class="idea-icon" viewBox="0 0 46 76" aria-hidden="true">
      <g fill="none" stroke="#1e1e1e" stroke-width="1.6" stroke-linecap="round">
        <line x1="23" y1="2" x2="23" y2="12"/>
        <line x1="8" y1="8" x2="13" y2="16"/>
        <line x1="38" y1="8" x2="33" y2="16"/>
        <line x1="1" y1="20" x2="8" y2="23"/>
        <line x1="45" y1="20" x2="38" y2="23"/>
        <path d="M 15 54 C 15 46 9 42 9 33 A 14 14 0 0 1 37 33 C 37 42 31 46 31 54 Z"/>
        <line x1="16" y1="58" x2="30" y2="58"/>
        <line x1="16" y1="62" x2="30" y2="62"/>
        <line x1="18" y1="66" x2="28" y2="66"/>
      </g>
    </svg>

    <ul class="service-list">
      <li><span class="bullet">•</span>Eye testing (Tallacor covered).</li>
      <li><span class="bullet">•</span>Prescription glasses,sunglasses<br>&amp; contact lenses.</li>
      <li><span class="bullet">•</span>All major health<br>funds accepted.</li>
    </ul>

    <div class="brand-mark" aria-hidden="true"></div>
    <p class="brand-name">Brookvane<br>Eyecare</p>

    <div class="illustration-slot" role="img" aria-label="Illustration of a woman adjusting her glasses"></div>

    <section class="contact-box">
      <svg class="phone-icon" viewBox="0 0 40 62" aria-hidden="true">
        <g fill="none" stroke="#1e1e1e" stroke-width="2">
          <rect x="6" y="14" width="26" height="44" rx="3" transform="rotate(-12 19 36)"/>
          <rect x="10" y="20" width="16" height="10" transform="rotate(-12 19 36)"/>
          <path d="M 3 10 Q 0 4 6 2"/>
          <path d="M 8 10 Q 6 6 10 5"/>
        </g>
        <g fill="#1e1e1e" transform="rotate(-12 19 36)">
          <rect x="11" y="35" width="4" height="3"/><rect x="17" y="35" width="4" height="3"/><rect x="23" y="35" width="4" height="3"/>
          <rect x="11" y="41" width="4" height="3"/><rect x="17" y="41" width="4" height="3"/><rect x="23" y="41" width="4" height="3"/>
          <rect x="11" y="47" width="4" height="3"/><rect x="17" y="47" width="4" height="3"/><rect x="23" y="47" width="4" height="3"/>
        </g>
      </svg>
      <div class="contact-lines">
        <p><span class="number">94517038</span> – 27 Harbour Crest Lane Claremont</p>
        <p><span class="number">95643218</span> – 86 Wattlegrove Road Subiaco</p>
      </div>
    </section>
  </main>
</body>
</html>
```